Flyer für Gästehaus am Bodensee
Zielgruppe
Es soll ein Hausprospekt in Form eines Wickelfalz Fylers (Standard Format, also 10x21 cm Endformat) für ein Gästehaus erstellt werden. Die Texte sollten von Ihnen erstellt werden. Dabei können Sie gerne die Texte der Internetseite (www.gaestehaus-wolkreiter.example) nutzen (entsprechend angepasst). Es werden auch zahlreiche Bilder vom Gästehaus und auch von Attraktionen in der Umgebung zur Verfügung gestellt (Wolkenfach Ablage: https://files.beispielablage.example/ordner?id=7KQ2ZtRmWpLx9NcVbDfGhJ). Diese dürfen aber nur für diese Ausschreibung verwendet werden!
Aufgabenstellung
- Der Flyer soll zeitlos sein (also auch in ein paar Jahren noch funktionieren)
- Der Flyer soll das Interesse am Haus und der Umgebung wecken (einige Ausflugsziele sollten erwähnt werden).
- Die Lage (Uhldingen-Mühlhofen bzw. Unteruhldingen) muss als Vorteil verkauft werden da von hier aus sehr viele Ausflugsziele gut erreicht werden können.
- Die Lage (quasi direkt am See) sollte erkenntlich sein.
- Die fertige Datei wird als PDF (für den Druck und für das Marketing) benötigt.
- Außerdem als Word Datei in der der Kunde selbst etwas ändern kann.
- Auch die Originaldatei von Ihrer Software möchten wir bei Abschluss erhalten.
- Alle Quelldateien (Bilder, Texte, Schriftarten usw.) gehen an uns über (inkl. aller Rechte und Lizenzen).
- Bitten nehmen Sie maximal ein Appartment als Beispiel im Flyer auf (es ist nicht zwangsläufig notwendig, es geht auch ganz ohne). In keinem Fall alle Appartments auflisten.

```html
<!DOCTYPE html>
<html lang="de">
<head>
<meta charset="utf-8">
<title>Gästehaus Wolkreiter – Wickelfalzflyer</title>
<link rel="stylesheet" href="https://fonts.googleapis.com/css2?family=Ubuntu:wght@400;500;700&family=Kalam:wght@300;400&display=swap">
<style>
  :root {
    --lake-blue: #1f5f8b;
    --lake-blue-dark: #184e74;
    --paper: #ffffff;
    --stage: #e6e6e6;
    --ink: #1f5f8b;
    --ink-soft: #2d6e99;
    --logo-grey: #7c8fa0;
  }
  * { box-sizing: border-box; margin: 0; padding: 0; }
  html, body { width: 1200px; height: 4079px; overflow: hidden; }
  body {
    background: var(--stage);
    font-family: "Ubuntu", Arial, sans-serif;
    color: var(--ink);
    position: relative;
  }
  .spread {
    position: absolute;
    left: 50px;
    width: 1100px;
    height: 776px;
    background: var(--paper);
    box-shadow: 0 14px 30px rgba(0,0,0,.28);
    display: grid;
    grid-template-columns: repeat(3, 1fr);
    overflow: hidden;
  }
  .spread--outside { top: 1180px; }
  .spread--inside  { top: 2120px; }
  .panel { position: relative; height: 776px; overflow: hidden; }
  .band { background: var(--lake-blue); color: #fff; position: absolute; left: 0; right: 0; }
  .photo { position: absolute; }
  .script-title {
    font-family: "Kalam", cursive;
    font-weight: 300;
    font-size: 24px;
    line-height: 1.1;
    white-space: nowrap;
  }
  .copy { font-size: 10.6px; line-height: 1.5; }
  .copy p + p { margin-top: 11px; }
  .copy b { font-weight: 700; }
  .text-block { position: absolute; left: 36px; right: 26px; }

  /* outside spread */
  .excursions .band { top: 0; height: 227px; padding: 38px 30px 0 36px; }
  .excursions .band .script-title { margin-bottom: 32px; }
  .excursions .band .copy { text-align: justify; }
  .collage { top: 227px; left: 0; right: 0; height: 260px; display: grid; grid-template-columns: 1fr 1fr; grid-template-rows: 1fr 1fr; gap: 3px; }
  .collage div { width: 100%; height: 100%; }
  .excursions .text-block { top: 512px; }

  .contact .band { top: 0; height: 227px; padding: 38px 30px 0 30px; }
  .contact .band .script-title { margin-bottom: 32px; }
  .contact .arrival { top: 255px; left: 30px; }
  .map { left: 30px; top: 390px; width: 310px; height: 326px; }

  .cover .logo { position: absolute; top: 70px; left: 0; right: 0; display: flex; align-items: center; justify-content: center; gap: 12px; }
  .cover .logo-name { font-family: "Ubuntu", Arial, sans-serif; font-weight: 400; font-size: 28px; color: var(--logo-grey); line-height: 1; }
  .cover .hero { top: 227px; left: 0; right: 0; height: 453px; }
  .cover .band { top: 680px; height: 96px; display: flex; align-items: center; justify-content: center; text-align: center; }
  .cover .band .script-title { font-size: 22px; line-height: 1.35; }

  /* inside spread */
  .house .band--top { top: 0; height: 326px; padding: 38px 30px 0 36px; }
  .house .band--top .script-title { margin-bottom: 28px; }
  .house .band--top .copy { text-align: justify; }
  .house .garden { top: 236px; left: 49px; width: 265px; height: 250px; border: 4px solid #fff; }
  .house .text-block { top: 506px; text-align: justify; }
  .house .band--foot { top: 692px; height: 84px; padding: 10px 36px 0; display: flex; align-items: center; gap: 12px; }
  .phone-label { font-size: 10.5px; }
  .phone-number { font-size: 17px; font-weight: 700; letter-spacing: .5px; }

  .rooms .living { top: 0; left: 0; right: 0; height: 326px; }
  .rooms .text-block { top: 366px; left: 32px; right: 28px; text-align: justify; }
  .rooms .bedroom { top: 589px; left: 0; right: 0; height: 187px; }

  .service .kitchen { top: 0; left: 0; right: 0; height: 326px; }
  .service .band { top: 326px; height: 263px; padding: 50px 26px 0; text-align: center; }
  .service .twin { top: 589px; left: 0; right: 0; height: 187px; }
</style>
</head>
<body>

<section class="spread spread--outside">
  <article class="panel excursions">
    <div class="band">
      <h2 class="script-title">Ausflugsziele</h2>
      <div class="copy">
        <p>Uhldingen-Mühlhofen selbst beherbergt zwei der schönsten Ausflugsziele am See: Besuchen Sie die <b>Pfahlbauten</b>, das größte und älteste archäologische Freilichtmuseum Süddeutschlands, oder machen Sie einen Abstecher zur <b>Barockkirche Birnau</b> mit ihrem traumhaften Blick über den Bodensee.</p>
      </div>
    </div>
    <div class="photo collage">
      <div role="img" aria-label="Foto: Pfahlbauten am Seeufer" style="background:linear-gradient(160deg,#b9cbd8,#8a6e4e)"></div>
      <div role="img" aria-label="Foto: Therme mit Außenbecken" style="background:linear-gradient(160deg,#6f9a4c,#4fa3c8)"></div>
      <div role="img" aria-label="Foto: Segelboote im Hafen" style="background:linear-gradient(160deg,#9fc3e6,#7c8a90)"></div>
      <div role="img" aria-label="Foto: Barockschloss mit Kirchturm" style="background:linear-gradient(160deg,#a9c9e8,#d9a07a 60%,#5c8a3a)"></div>
    </div>
    <div class="text-block copy">
      <p>Weltbekannt ist die <b>Blumeninsel Mainau</b>, die Sie im Frühling und im Herbst, vom Gästehaus Wolkreiter aus sehen können. Machen Sie einen Spaziergang zur Schiffsanlegestelle in Unteruhldingen, fahren Sie dann mit dem Schiff hinüber und genießen Rosen und Orchideen und im Schmetterlingshaus die exotischsten Schmetterlinge!</p>
      <p>Wenn Sie Geschichte und die Romantik alter Schlösser und Burgen lieben, dann gefällt Ihnen sicher <b>Überlingen, die alte Reichsstadt</b> mit den schönen Fachwerkhäusern, in der man auch gut einkaufen kann. Für Ihr Verwöhnprogramm stehen die <b>Thermen in Meersburg und Überlingen</b> mit ihren Wellnesslandschaften bereit.</p>
    </div>
  </article>

  <article class="panel contact">
    <div class="band">
      <h2 class="script-title">Gästehaus Wolkreiter</h2>
      <div class="copy">
        <p>Seeblickweg 4 &nbsp;|&nbsp; 88690 Uhldingen-Mühlhofen</p>
        <p style="margin-top:10px">Tel.: &nbsp;0 75 00 / 41 28 &nbsp;|&nbsp; Fax: 0 75 00 / 41 29<br>
        E-Mail: info@gaestehaus-wolkreiter.example<br>
        Web: www.gaestehaus-wolkreiter.example</p>
      </div>
    </div>
    <div class="text-block copy arrival">
      <p>Für Gäste, die mit dem Auto anreisen, stehen Parkplätze direkt vor dem Haus zur Verfügung. Wer mit der Bahn zu uns kommt, wird auf Wunsch vom Bahnhof in Oberuhldingen abgeholt.</p>
      <p>Wir freuen uns auf Sie! <b>Ihre Familie Wolkreiter</b></p>
    </div>
    <div class="photo map" role="img" aria-label="Lageplan: Seeufer mit Pfahlbauten, Bahnhof Uhldingen-Mühlhofen, Gästehaus, A31, Meersburg und Überlingen" style="background:linear-gradient(90deg,#2f7aa8 0 32%,#f1f1f1 32%)"></div>
  </article>

  <article class="panel cover">
    <div class="logo">
      <svg width="16" height="16" viewBox="0 0 16 16" aria-hidden="true"><circle cx="8" cy="8" r="7" fill="var(--logo-grey)"/></svg>
      <span class="logo-name">Gästehaus Wolkreiter</span>
    </div>
    <div class="photo hero" role="img" aria-label="Foto: Gästehaus mit Balkonen, Blumenkästen und Rasen" style="background:linear-gradient(180deg,#dfe4ea 0,#c87b52 30%,#e9e4dc 55%,#6f9c3e 80%,#5d8f34)"></div>
    <div class="band">
      <p class="script-title">Ihr Gästehaus in<br>direkter Nähe zum Bodensee</p>
    </div>
  </article>
</section>

<section class="spread spread--inside">
  <article class="panel house">
    <div class="band band--top">
      <h2 class="script-title">Gästehaus &amp; Appartements</h2>
      <div class="copy">
        <p>Das Gästehaus Wolkreiter liegt in einer der schönsten Urlaubsgegenden der Bodensee-Region, in <b>Unteruhldingen</b>, zwischen Meersburg und Überlingen, nur <b>50 Meter vom See entfernt</b>, gegenüber der Blumeninsel Mainau. Die schönsten Ausflugsziele am See erreichen Sie innerhalb kurzer Zeit.</p>
      </div>
    </div>
    <div class="photo garden" role="img" aria-label="Foto: Gästehaus mit Liegewiese und Sonnenschirm" style="background:linear-gradient(180deg,#dfe6ee 0,#b9643e 35%,#ece6da 60%,#6c9c3a 85%)"></div>
    <div class="text-block copy">
      <p>Unsere schöne Liegewiese und der gepflegte Garten sind das richtige Ambiente, wenn Sie sich erholen und ein wenig die Seele baumeln lassen wollen oder nach einem ereignisreichen Urlaubstag sich noch mit anderen Gästen zu einem kleinen Plausch treffen möchten.</p>
      <p>Ob Sie geschäftlich unterwegs sind oder Ihren Urlaub bei uns verbringen, wir sind stets bemüht, dass Sie sich bei uns wohl fühlen. Bei uns erwartet Sie eine herzliche und familiäre Atmosphäre.</p>
    </div>
    <div class="band band--foot">
      <svg width="20" height="20" viewBox="0 0 24 24" aria-hidden="true"><path fill="#fff" d="M6.6 10.8a15.1 15.1 0 0 0 6.6 6.6l2.2-2.2a1 1 0 0 1 1-.25 11.4 11.4 0 0 0 3.6.57 1 1 0 0 1 1 1V20a1 1 0 0 1-1 1A17 17 0 0 1 3 4a1 1 0 0 1 1-1h3.5a1 1 0 0 1 1 1c0 1.250.2 2.45.57 3.57a1 1 0 0 1-.25 1z"/></svg>
      <div>
        <div class="phone-label">Rufen Sie uns gerne an:</div>
        <div class="phone-number">0 75 00 / 41 28</div>
      </div>
    </div>
  </article>

  <article class="panel rooms">
    <div class="photo living" role="img" aria-label="Foto: Appartement-Wohnraum mit Esstisch und Sofa" style="background:linear-gradient(170deg,#e8e3da 0,#d7cab4 45%,#c46a3f 70%,#5a3a2a)"></div>
    <div class="text-block copy">
      <p>Unsere Zimmer und Appartements sind komfortabel ausgestattet, damit Sie einen angenehmen und entspannten Urlaub verbringen. Alle Appartements verfügen über eine <b>Dusche / WC, Küche, Balkon</b> (teilweise mit Seesicht) oder <b>Terrasse. TV, Telefon, W-LAN, Safe, Bettwäsche</b> und <b>Handtücher</b> gehören ebenso zur Ausstattung und sind inklusiv.</p>
      <p>Wir haben ausschließlich Nichtraucherzimmer. Gerne können Sie auf dem Balkon oder der Terrasse rauchen. Bitte beachten Sie außerdem, dass in unserem Haus keine Tiere gestattet sind.</p>
    </div>
    <div class="photo bedroom" role="img" aria-label="Foto: Doppelzimmer mit Holzbett" style="background:linear-gradient(180deg,#e7dfd2,#c9a475 55%,#d46b52)"></div>
  </article>

  <article class="panel service">
    <div class="photo kitchen" role="img" aria-label="Foto: Küchenzeile im Appartement" style="background:linear-gradient(160deg,#efe9e0 0,#cdbfae 45%,#a9a6a2 75%,#6a4a34)"></div>
    <div class="band">
      <div class="copy">
        <p>Auf Wunsch verwöhnen wir Sie auch<br>mit einem reichhaltigen Frühstück.</p>
        <p>Am Anreisetag stehen die Appartements<br>ab 13.00 Uhr und am Abreisetag<br>bis 10.00 Uhr zur Verfügung.</p>
      </div>
    </div>
    <div class="photo twin" role="img" aria-label="Foto: Schlafzimmer mit weißer Bettwäsche" style="background:linear-gradient(160deg,#ede8e0,#c4703f 45%,#f3f1ee 70%)"></div>
  </article>
</section>

</body>
</html>
```